Visitenkarten-Design für Catering/ Liefertouren
Vielen Dank für die professionelle Zusammenarbeit. Änderungen wurden schnell und treffend umgesetzt. Wir sind mit dem Ergebnis sehr zufrieden.
Zielgruppe
Catering/ Liefertouren für hochwertige selbstgemachte Quiches/ französische Tartes, Suppen, Currys
Aufgabenstellung
2 Visitenkarten im Format DIN6 (21x10,5) lang die sich auf der 1. (Bild) Seite unterscheiden aber mit identischer 2. Seite.
Karte 'Quiche' 1. Seite:
'Quiche '
Fait Maison - depuis 2011
Quiches, Soups, Currys,
Catering, Abholung, Liefertouren
www.Kovendo.de,
info@kovendo.de
Karte 'Soups' 1. Seite:
'KovendoChicken, KovendoTofu'
2. Seite (für beide Karten identisch)
Seite soll eine Art Vorlage sein und besteht lediglich aus einer gestalterischen 'Umrahmung' und unserem Logo am unteren Seitenrand. Der Durchmesser des Logos soll max. 15% der gesamten Seitenlänge betragen.
Seite wird von uns mit Angeboten/ Aktionen bedruckt in kleiner Stückzahl nachträglich bedruckt.
1. Seiten (Quer- oder Hochformat je nach Bild möglich).
2. Seite im Hochformat.
Keine Vorgaben bzgl. Schrifttyp.

```html
<!DOCTYPE html>
<html lang="de">
<head>
<meta charset="utf-8">
<title>Kovendo – Visitenkarten</title>
<link href="https://fonts.googleapis.com/css2?family=Sorts+Mill+Goudy&family=Open+Sans:wght@400&display=swap" rel="stylesheet">
<style>
  :root {
    --page: #ffffff;
    --card: #050b16;
    --ink: #ffffff;
    --accent: #c8202a;
    --brand-brown: #4a2a20;
    --quiche-a: #6b7a3a;
    --quiche-b: #c08a4a;
    --quiche-c: #1c2a3a;
    --soup-a: #b8322a;
    --soup-b: #4f7a2c;
    --soup-c: #5c5f63;
  }
  * { margin: 0; padding: 0; box-sizing: border-box; }
  html, body { width: 1200px; height: 532px; overflow: hidden; background: var(--page); }
  .sheet { position: relative; width: 1200px; height: 532px; }
  .card {
    position: absolute; top: 27px; width: 345px; height: 483px;
    background: var(--card); overflow: hidden; color: var(--ink);
  }
  .card--quiche { left: 55px; }
  .card--soups { left: 427px; }
  .card--back { left: 800px; }
  .card__title {
    position: absolute; top: 18px; left: 0; width: 100%; text-align: center;
    font-family: "Sorts Mill Goudy", serif; font-weight: 400; font-size: 39px; line-height: 1; letter-spacing: 1px;
  }
  .card__tagline {
    position: absolute; top: 77px; left: 0; width: 100%; text-align: center;
    font-family: "Sorts Mill Goudy", serif; font-size: 10px;
  }
  .card--soups .card__tagline { top: 74px; }
  .card__services {
    position: absolute; top: 104px; left: 0; width: 100%; text-align: center;
    font-family: "Open Sans", sans-serif; font-size: 9px; letter-spacing: 0.1px; white-space: nowrap;
  }
  .card--soups .card__services { top: 105px; }
  .card__services .sep { color: var(--accent); margin: 0 2px; }
  .card__photo { position: absolute; left: 0; top: 142px; width: 345px; height: 290px; }
  .card__contact {
    position: absolute; top: 445px; left: 0; width: 100%; height: 26px;
    display: flex; justify-content: center; align-items: center;
    font-family: "Sorts Mill Goudy", serif; font-size: 10.5px; white-space: nowrap;
  }
  .card__contact span { padding: 0 11px; }
  .card__contact .rule { width: 1px; height: 26px; background: var(--accent); padding: 0; }
  .back-frame { position: absolute; left: 0; top: 0; }
  .brand {
    position: absolute; left: 130px; top: 368px; width: 94px; height: 94px; border-radius: 50%;
    background: var(--brand-brown); border: 2px solid var(--ink);
    display: flex; align-items: center; justify-content: center;
    font-family: "Sorts Mill Goudy", serif; font-size: 20px; color: var(--ink);
  }
</style>
</head>
<body>
<div class="sheet">

  <section class="card card--quiche">
    <h1 class="card__title">Quiche</h1>
    <p class="card__tagline">Fait Maison - depuis 2011</p>
    <p class="card__services">QUICHES<span class="sep">|</span>SOUPS<span class="sep">|</span>CURRYS<span class="sep">|</span>CATERING<span class="sep">|</span>ABHOLUNG<span class="sep">|</span>LIEFERTOUREN</p>
    <svg class="card__photo" viewBox="0 0 345 290" role="img" aria-label="Foto: Spinat-Quiche mit Tortenheber auf Gitterrost, dunkler Hintergrund">
      <defs>
        <radialGradient id="quicheTone" cx="0.62" cy="0.5" r="0.6">
          <stop offset="0" stop-color="var(--quiche-a)"/>
          <stop offset="0.6" stop-color="var(--quiche-b)"/>
          <stop offset="1" stop-color="var(--quiche-c)"/>
        </radialGradient>
      </defs>
      <path d="M0 0 C120 -4 260 0 345 40 L345 280 C250 292 130 280 40 240 C10 220 0 200 0 180 Z" fill="url(#quicheTone)"/>
    </svg>
    <div class="card__contact">
      <span>www.kovendo.de</span><span class="rule"></span>
      <span>+49 (0) 89-2741 5830</span><span class="rule"></span>
      <span>info@kovendo.de</span>
    </div>
  </section>

  <section class="card card--soups">
    <h1 class="card__title">Soups</h1>
    <p class="card__tagline">Fait Maison - depuis 2011</p>
    <p class="card__services">QUICHES<span class="sep">|</span>SOUPS<span class="sep">|</span>CURRYS<span class="sep">|</span>CATERING<span class="sep">|</span>ABHOLUNG<span class="sep">|</span>LIEFERTOUREN</p>
    <svg class="card__photo" viewBox="0 0 345 290" role="img" aria-label="Foto: Tomatensuppe mit Croutons im gusseisernen Topf, umgeben von Paprika, Kräutern und Gewürzen">
      <defs>
        <radialGradient id="soupTone" cx="0.5" cy="0.5" r="0.6">
          <stop offset="0" stop-color="var(--soup-a)"/>
          <stop offset="0.5" stop-color="var(--soup-c)"/>
          <stop offset="1" stop-color="var(--soup-b)"/>
        </radialGradient>
      </defs>
      <path d="M0 0 C80 -2 220 -2 300 20 C330 40 345 60 345 80 L345 286 C240 290 120 288 50 250 C15 225 0 200 0 180 Z" fill="url(#soupTone)"/>
    </svg>
    <div class="card__contact">
      <span>www.kovendo.de</span><span class="rule"></span>
      <span>+49 (0) 89-2741 5830</span><span class="rule"></span>
      <span>info@kovendo.de</span>
    </div>
  </section>

  <section class="card card--back">
    <svg class="back-frame" width="345" height="483" viewBox="0 0 345 483" aria-hidden="true">
      <path d="M56 445 H16.5 V17 H330 V445 H302" fill="none" stroke="var(--ink)" stroke-width="1"/>
    </svg>
    <div class="brand">Kovendo</div>
  </section>

</div>
</body>
</html>
```